Providing Back Office Solutions to Financial Advisors and Attorney Needs a Business Card Design

Need a Business Card Design that speaks to Financial Advisor and Attorneys. Some of the word that come to mind is Clean/Simple & Futuristic.

Industry/Entity Type

Business

```html
<!DOCTYPE html>
<html lang="en">
<head>
<meta charset="utf-8">
<title>Veritan Back Office Solutions – Business Card</title>
<link rel="stylesheet" href="https://fonts.googleapis.com/css2?family=Open+Sans:wght@400;600;700&family=Arimo:wght@400&display=swap">
<style>
  :root {
    --stage: #b3b3b3;
    --paper: #ffffff;
    --brand: #1a5fd6;
    --navy: #0b2596;
    --sky: #1d8be6;
    --ink: #111111;
    --back-top: #0648b8;
    --back-bottom: #2a9ef2;
  }
  * { margin: 0; padding: 0; box-sizing: border-box; }
  html, body { width: 1200px; height: 414px; overflow: hidden; background: var(--stage); }
  .canvas { position: relative; width: 1200px; height: 414px; }

  .card { position: absolute; top: 45px; width: 552px; height: 334px; overflow: hidden; }
  .card--front { left: 39px; background: var(--paper); }
  .card--back { left: 616px; background: linear-gradient(170deg, var(--back-top) 0%, #0f6ad8 55%, var(--back-bottom) 100%); }

  .brand { position: absolute; font-family: "Open Sans", sans-serif; }
  .brand__mark { position: absolute; }
  .brand__name { position: absolute; font-weight: 600; letter-spacing: 0.06em; line-height: 1; white-space: nowrap; }
  .brand__tagline { position: absolute; font-weight: 600; line-height: 1; white-space: nowrap; }

  .card--front .brand__mark { left: 40px; top: 52px; width: 64px; height: 64px; background: var(--brand); }
  .card--front .brand__name { left: 127px; top: 62px; font-size: 41px; color: var(--brand); }
  .card--front .brand__tagline { left: 130px; top: 119px; font-size: 15px; color: var(--brand); }

  .card--back .brand__mark { left: 64px; top: 118px; width: 98px; height: 98px; background: var(--paper); }
  .card--back .brand__name { left: 196px; top: 125px; font-size: 62px; color: var(--paper); }
  .card--back .brand__tagline { left: 199px; top: 201px; font-size: 21px; color: var(--paper); }

  .person { position: absolute; left: 65px; top: 213px; font-family: "Open Sans", sans-serif; }
  .person__name { font-size: 22px; font-weight: 700; color: var(--navy); line-height: 1.1; }
  .person__role { font-size: 12px; color: var(--ink); text-align: right; margin-top: 3px; }

  .contact { position: absolute; left: 273px; top: 172px; font-family: "Arimo", Arial, sans-serif; color: var(--ink); }
  .contact__address { font-size: 14.5px; line-height: 18px; }
  .contact__list { list-style: none; margin-top: 7px; }
  .contact__item { display: flex; align-items: center; gap: 10px; font-size: 14.5px; height: 24px; }
  .contact__item--web { font-size: 13px; margin-top: 2px; }
  .contact__icon { width: 16px; height: 16px; flex: none; }

  .card__band { position: absolute; left: 0; bottom: 0; width: 552px; height: 21px; }
</style>
</head>
<body>
<main class="canvas">

  <section class="card card--front" aria-label="Card front">
    <div class="brand">
      <span class="brand__mark"></span>
      <span class="brand__name">VERITAN</span>
      <span class="brand__tagline">BACK OFFICE SOLUTIONS</span>
    </div>

    <div class="person">
      <p class="person__name">Daniel Reyes</p>
      <p class="person__role">President</p>
    </div>

    <div class="contact">
      <p class="contact__address">1420 Harbor View Lane<br>Seaport, CA &nbsp;&nbsp;90000</p>
      <ul class="contact__list">
        <li class="contact__item">
          <svg class="contact__icon" viewBox="0 0 16 16" aria-hidden="true">
            <circle cx="8" cy="8" r="8" fill="var(--navy)"/>
            <path d="M5.2 4.2l1.6-.4.8 2-1 .8c.5 1.2 1.3 2 2.5 2.5l.8-1 2 .8-.4 1.6c-3.6.2-6.5-2.7-6.3-6.3z" fill="#fff"/>
          </svg>
          555 014 2290
        </li>
        <li class="contact__item">
          <svg class="contact__icon" viewBox="0 0 16 16" aria-hidden="true">
            <rect x="1" y="3.5" width="14" height="9.5" fill="var(--navy)"/>
            <path d="M1.5 4l6.5 5 6.5-5" stroke="#fff" stroke-width="1.2" fill="none"/>
          </svg>
          daniel.reyes@veritanbo.com
        </li>
        <li class="contact__item contact__item--web">
          <svg class="contact__icon" viewBox="0 0 16 16" aria-hidden="true">
            <circle cx="8" cy="8" r="7.5" fill="var(--navy)"/>
            <ellipse cx="8" cy="8" rx="3" ry="7" stroke="#fff" stroke-width="1" fill="none"/>
            <path d="M1 8h14M2.5 4.5h11M2.5 11.5h11" stroke="#fff" stroke-width="1"/>
          </svg>
          www.veritanbo.com
        </li>
      </ul>
    </div>

    <svg class="card__band" viewBox="0 0 552 21" preserveAspectRatio="none" aria-hidden="true">
      <polygon points="0,0 324,0 330,21 0,21" fill="var(--navy)"/>
      <polygon points="328,0 552,0 552,21 334,21" fill="var(--sky)"/>
    </svg>
  </section>

  <section class="card card--back" aria-label="Card back">
    <div class="brand">
      <span class="brand__mark"></span>
      <span class="brand__name">VERITAN</span>
      <span class="brand__tagline">BACK OFFICE SOLUTIONS</span>
    </div>
  </section>

</main>
</body>
</html>
```